Tallant Family Adoption Fundraiser

The sole purpose of this card is to tell people about the fundraiser and direct them to the website that will allow them to participate.  No other contact information is needed.
Since our approach is through personal networking, this card is our sole marketing piece and needs to be effective.  We will use an image of the card for the email & Facebook outreaches we will do.  We have a very limited budget (thus the fundraiser).
We will need a quantity of 2,000 cards.  We dont need to pay for high gloss or metalic finishes, but we were thinking we probably would want a folded business card to give us more real estate to work with.
About the fundraiser (will help you understand the content needed):  Our family is adopting a young girl from Colombia, South America.  We need to raise about $15,000 to bring her home.  This fundraiser is something called a "Duck Race".  People will go to our website and 'purchase' ducks for the race.  For each duck, there will be a rubber duck in the 'race' with their own unique number on it.  On the day of the race, all of the ducks are dumped into a river.  The first ones to cross the finish line down stream is the winner.  The more ducks people put in the race in their name, the more chances they have to win the cash prizes.  We will video the race, and show it on our website.  The idea was to make this an effective and low maintenance fundraiser - nobody has to attend an event - people dont even need to know us, they only need to want to have a chance at the cash prize.  With that being said, here are some ideas of content:
- title:  "The Splendid Paddle Dash"
- "Win 1 of 3 cash prizes totalling $1,000
- www.Welcoming Little Sparrow Back.example
- The Tallant family is adopting a young girl from Colombia, South America, and needs your help to bring her home.
-  We could include a picture of her.
-  We have an icon of a Duck holding a Colombian flag - this is an icon our son created and must be used as the focal point.  We want our existing kids (3 boys) to be part of this and our son Corwin love computer animation and drawing - he created the icon.
-  People can sponsor a duck in the race or simply make their own, individual donation through the website.
-  We are using duck puns like crazy - we will even have a duck pun contest and the winners get free additional ducks in the race.
-  We want our network to be able to use these cards to get others to participate because of the cause - even if they do not know us.  That is why we thought the folded cards would be good because we would have space to put our testimony.  If cost-prohibitive, then we will settle for a 2-sided card.
We are open to suggestions, but time is absolutely of the essence.  We just got approved by Colombia, but we only have 2 weeks left to network with folks in our schools before they are done for the year.  We need a very quick turn-around.

Updates
Due to a browser issue, the icon was not uploaded in my brief.  They are in the process of manually adding it to my brief now and should be available shortly. Thank you for your help.

Target Market(s)
Potential donors/sponsors
Industry/Entity Type
Real Estate
Contact Information for Business Card
www.WelcomingLittleSparrowBack.example
Requirements
Must have
- Catchy but simple exterior to make people want to see the interior of a folded business card.

```html
<!DOCTYPE html>
<html lang="en">
<head>
<meta charset="utf-8">
<title>Tallant Family Adoption Fun-Raiser Card</title>
<link rel="stylesheet" href="https://fonts.googleapis.com/css2?family=Asap+Condensed:ital,wght@1,400;1,700&display=swap">
<style>
  :root {
    --ray-light: #fffbe0;
    --ray-mid: #fbee9a;
    --ray-deep: #f3dc4a;
    --ink: #262626;
    --alert-red: #e3161d;
    --banner-blue: #1d6fc0;
    --banner-blue-dark: #0d4f96;
    --banner-cyan: #35b7ea;
    --white: #ffffff;
    --duck-yellow: #f7e33a;
    --flag-blue: #2b3f9b;
    --flag-red: #d9262c;
    --photo-frame: #7a6d94;
    --photo-fill: #e9e4ea;
  }

  html, body {
    margin: 0;
    padding: 0;
    width: 1200px;
    height: 702px;
    overflow: hidden;
    background: var(--white);
  }

  .card {
    position: relative;
    width: 1200px;
    height: 702px;
    overflow: hidden;
    font-family: "Asap Condensed", "Arial Narrow", sans-serif;
    font-style: italic;
    color: var(--ink);
  }

  .card__backdrop {
    position: absolute;
    inset: 0;
    background: radial-gradient(circle at 46% 42%, var(--ray-light) 0%, var(--ray-mid) 45%, var(--ray-deep) 100%);
  }

  .mascot {
    position: absolute;
    left: 39px;
    top: 61px;
    width: 326px;
    height: 603px;
    border-radius: 40% 40% 45% 45% / 25% 25% 40% 40%;
    background: linear-gradient(180deg, var(--duck-yellow) 0%, var(--duck-yellow) 62%, var(--flag-blue) 72%, var(--flag-red) 86%);
  }

  .story {
    position: absolute;
    left: 404px;
    top: 76px;
    width: 730px;
    text-align: center;
    font-size: 25px;
    line-height: 22.9px;
    letter-spacing: -0.2px;
  }

  .story__line {
    display: block;
    white-space: nowrap;
  }

  .story__heading {
    font-weight: 700;
  }

  .story__offer {
    color: var(--alert-red);
  }

  .web-banner {
    position: absolute;
    left: 518px;
    top: 568px;
    width: 456px;
    height: 58px;
  }

  .web-banner svg {
    position: absolute;
    inset: 0;
  }

  .web-banner__address {
    position: absolute;
    inset: 0;
    display: flex;
    align-items: center;
    justify-content: center;
    color: var(--white);
    font-style: normal;
    font-weight: 700;
    font-size: 21px;
    letter-spacing: -0.2px;
    padding-bottom: 4px;
  }

  .portrait {
    position: absolute;
    left: 1014px;
    top: 518px;
    width: 110px;
    height: 120px;
    box-sizing: border-box;
    border: 1.5px solid var(--photo-frame);
    background: linear-gradient(180deg, var(--photo-fill) 0%, #f7f5f6 100%);
  }
</style>
</head>
<body>
<main class="card">
  <div class="card__backdrop" role="img" aria-label="Yellow sunburst rays radiating across the background"></div>

  <div class="mascot" role="img" aria-label="Cartoon rubber duck in sunglasses wearing Colombian colours and waving the Colombian flag"></div>

  <section class="story">
    <span class="story__line">Lucia is 7 years old and lives in Colombia, South</span>
    <span class="story__line">America. She is waiting to go home to her forever family.</span>
    <span class="story__line">The adoption is finalized, and the Tallant family appreci-</span>
    <span class="story__line">ates your support to help bring her home.&nbsp; See our web-</span>
    <span class="story__line">site for more about Lucia, our family, and our journey.</span>
    <span class="story__line story__heading">‘FUN’-RAISER</span>
    <span class="story__line story__offer">A virtual event where you can win one of (3) cash</span>
    <span class="story__line story__offer">prizes totaling $1,000</span>
    <span class="story__line">Its easy and fun – a real quack-up!&nbsp; You decide how</span>
    <span class="story__line">many rubber ducks you want to enter into the race.&nbsp; A</span>
    <span class="story__line">unique number is written on the bottom of your duck(s).</span>
    <span class="story__line">All ducks are dropped off of a bridge, and race down-</span>
    <span class="story__line">stream.&nbsp; The first (3) that arrive at the finish area win.</span>
    <span class="story__line">Return to our website after the event and watch it on</span>
    <span class="story__line">video.&nbsp; The more ducks you enter, the more chance you</span>
    <span class="story__line">have to win.&nbsp; Everything is done online – enter the race</span>
    <span class="story__line">or make a private donation.&nbsp; Check out the website to</span>
    <span class="story__line">find out how you can also win bonus ducks entered into</span>
    <span class="story__line">the race for you for free.</span>
    <span class="story__line">Good luck to your duck!</span>
  </section>

  <div class="web-banner">
    <svg width="456" height="58" viewBox="0 0 456 58" aria-hidden="true">
      <defs>
        <linearGradient id="bannerFill" x1="0" y1="0" x2="0" y2="1">
          <stop offset="0" stop-color="var(--banner-blue)"/>
          <stop offset="1" stop-color="var(--banner-blue-dark)"/>
        </linearGradient>
      </defs>
      <polygon points="6,4 456,0 448,46 0,58" fill="url(#bannerFill)"/>
      <polygon points="0,58 448,46 446,52 2,58" fill="var(--banner-cyan)"/>
    </svg>
    <span class="web-banner__address">www.WelcomingLittleSparrowBack.example</span>
  </div>

  <div class="portrait" role="img" aria-label="Portrait photo of Lucia"></div>
</main>
</body>
</html>
```